Create PP presentation that explains the one on one on camera video series that features the world's top real estate developers, builders, investors, banks, lawyers, academics and policy makers. It will be a hard hitting frank discussion about the real issues that the COMMERCIAL (not residential) real estate industry is dealing with. The marketing should be news network looking with high tech look and feel and show that it is provides serious and useful financial news content. We are a commercial real estate firm that has established a media arm to provide REAL TIME information regarding the real estate market place. Examples of look and feel should be KWTAV or Harvelt TV. Two pp have been attached should be able to tell that they are from the same company but encourage to take your own approach. A full pp presentation has been included title Sundial Interviews - make it your own. You do not have to use the same images that were provided, these are just guidelines as to what we want to communicate. The layout can be changed - we are using bullet points but if you have a better way to present the information, please do so.

```html
<!DOCTYPE html>
<html lang="en">
<head>
<meta charset="utf-8">
<title>Sponsorship Opportunities</title>
<link rel="stylesheet" href="https://fonts.googleapis.com/css2?family=Roboto:wght@300;400;700&family=Roboto+Condensed:wght@700&display=swap">
<style>
  :root {
    --header-top: #eef6fb;
    --header-bottom: #c9e6f5;
    --title-dark: #3a3d40;
    --title-blue: #1a7fe0;
    --rule: #ffffff;
    --glass-deep: #1d4f86;
    --glass-mid: #3f86c7;
    --glass-light: #b9d7ee;
    --panel: rgba(255, 255, 255, 0.86);
    --body-text: #3c3c3c;
    --footer: #4a4a4a;
    --footer-text: #ffffff;
    --brand-box: #ffffff;
    --brand-green: #38b449;
  }
  * { margin: 0; padding: 0; box-sizing: border-box; }
  html, body { width: 1200px; height: 900px; overflow: hidden; background: #ffffff; }
  .slide {
    position: relative;
    width: 1200px;
    height: 900px;
    overflow: hidden;
    font-family: "Roboto", Arial, sans-serif;
  }
  .slide-header {
    position: absolute;
    left: 0; top: 0;
    width: 1200px; height: 104px;
    background: linear-gradient(180deg, var(--header-top) 0%, var(--header-bottom) 100%);
    border-bottom: 3px solid var(--rule);
    display: flex;
    align-items: center;
    padding-left: 34px;
  }
  .slide-title {
    font-family: "Roboto Condensed", "Arial Narrow", sans-serif;
    font-weight: 700;
    font-size: 39px;
    color: var(--title-dark);
    letter-spacing: -0.2px;
  }
  .slide-title .accent { color: var(--title-blue); }
  .backdrop {
    position: absolute;
    left: 0; top: 107px;
    width: 1200px; height: 725px;
    background:
      linear-gradient(115deg, var(--glass-light) 0%, var(--glass-mid) 30%, var(--glass-deep) 52%, var(--glass-mid) 70%, var(--glass-light) 86%, var(--glass-mid) 100%);
  }
  .tier-panel {
    position: absolute;
    left: 33px; top: 182px;
    width: 713px; height: 592px;
    background: var(--panel);
    padding: 21px 0 0 30px;
    color: var(--body-text);
    font-weight: 300;
    font-size: 20.5px;
    line-height: 33px;
  }
  .tier + .tier { margin-top: 33px; }
  .tier-name { font-weight: 700; }
  .tier-details { list-style: none; }
  .slide-footer {
    position: absolute;
    left: 0; top: 832px;
    width: 1200px; height: 68px;
    background: var(--footer);
  }
  .copyright {
    position: absolute;
    left: 21px; top: 0;
    line-height: 68px;
    font-size: 20px;
    font-weight: 300;
    color: var(--footer-text);
  }
  .brand {
    position: absolute;
    left: 915px; top: 832px;
    width: 285px; height: 68px;
    background: var(--brand-box);
    display: flex;
    align-items: center;
    justify-content: center;
  }
  .brand-name {
    font-family: "Roboto", Arial, sans-serif;
    font-weight: 700;
    font-size: 40px;
    letter-spacing: -1px;
    color: var(--brand-green);
  }
</style>
</head>
<body>
<div class="slide">
  <header class="slide-header">
    <h1 class="slide-title">Pre – November 1, 2014 – <span class="accent">Sponsorship Opportunities</span></h1>
  </header>

  <div class="backdrop" role="img" aria-label="Photograph of a modern glass office tower facade with blue reflective panels"></div>

  <section class="tier-panel">
    <div class="tier">
      <h2 class="tier-name">Gold Sponsor</h2>
      <ul class="tier-details">
        <li>$25,000 (before November 1, 2014) - $100,000 (After November 1, 2014)</li>
        <li>Single sponsor for six videos in 2014 / 2015</li>
        <li>Single company logo appears on Flash report for six weeks</li>
        <li>National on-line campaign – six weeks</li>
      </ul>
    </div>
    <div class="tier">
      <h2 class="tier-name">Silver Sponsor</h2>
      <ul class="tier-details">
        <li>$12,000(before November 1, 2014) - $48,000 (After November 1, 2014)</li>
        <li>Shared sponsor for three videos in 2014 / 2015</li>
        <li>Shared sponsorship logos appears on Flash report for two weeks</li>
        <li>National on-line campaign – three weeks</li>
      </ul>
    </div>
    <div class="tier">
      <h2 class="tier-name">Bronze Sponsor</h2>
      <ul class="tier-details">
        <li>$1,500 (before November 1, 2014) - $6,000 (After November 1, 2014)</li>
        <li>Up to eights sponsor for one video in 2014 / 2015</li>
        <li>Logos appears on Flash report for one weeks</li>
        <li>National on-line campaign – one week</li>
      </ul>
    </div>
  </section>

  <footer class="slide-footer">
    <p class="copyright">Copyright text here</p>
  </footer>
  <div class="brand">
    <span class="brand-name">Stratavue</span>
  </div>
</div>
</body>
</html>
```